Company Website

We require an online clothing store website for construction workwear.
It needs to be easy to read, user friendly, easy to navigate purchasing.
We are after designs incorporating our recently design logo, and colour combinations black white and orange (same as the company logo). Needs to highlight quality, safety and products. Any ideas around highlighting branding are welcome.

Target Market(s)

Construction workers and businesses.

Industry/Entity Type

Construction

Coding

Coded - Design and coding required

Number of Pages Required

5+ page

Colors
EE7325
F08F49
F5BC92
FAE3D3
FDF4ED

Requirements
Must have
• Include all pictures, prices and details of the products we sell. See PDF uploaded to brief.
Nice to have
• Simple access to purchase items. Easy to navigate website layout.

```html
<!DOCTYPE html>
<html lang="en">
<head>
<meta charset="utf-8">
<title>Ironline Workwear – Construction Workwear Store</title>
<link href="https://fonts.googleapis.com/css2?family=Archivo+Black&family=Caveat+Brush&family=Roboto:wght@400;500;700&display=swap" rel="stylesheet">
<style>
:root{
  --orange:#ee7325;
  --orange-2:#f08f49;
  --orange-3:#f5bc92;
  --orange-4:#fae3d3;
  --orange-5:#fdf4ed;
  --ink:#222;
  --dark:#2c2c2c;
  --hero-grey:#4b4b4b;
  --hero-light:#eceded;
  --hero-green:#a8bf86;
  --about-bg:#f3f8e3;
  --footer:#353535;
  --white:#fff;
}
*{box-sizing:border-box;margin:0;padding:0}
html,body{width:1200px;height:4119px;overflow:hidden}
body{font-family:"Roboto",sans-serif;color:var(--ink);background:var(--white);position:relative}
.abs{position:absolute}
.heavy{font-family:"Archivo Black",sans-serif}
.script{font-family:"Caveat Brush",cursive}

/* header */
.site-header{position:absolute;top:0;left:0;width:1200px;height:75px;background:var(--white)}
.brand{position:absolute;left:115px;top:18px;font-family:"Archivo Black",sans-serif;color:var(--orange);font-size:24px;letter-spacing:2px;line-height:1}
.brand small{display:block;font-size:10px;letter-spacing:6px;margin-top:4px;padding-left:60px}
.account{position:absolute;left:690px;top:26px;font-size:14px;display:flex;align-items:center;gap:8px}
.account a{color:var(--orange)}
.cart{position:absolute;left:872px;top:24px}
.search{position:absolute;left:923px;top:22px;width:166px;height:30px;border-radius:15px;background:#ccc;font-size:13px;color:#666;padding:7px 14px}
.search svg{position:absolute;right:12px;top:7px}

.main-nav{position:absolute;top:75px;left:0;width:1200px;height:51px;background:var(--dark);display:flex;align-items:center;padding-left:110px;gap:30px}
.main-nav span{color:#fff;font-size:14px;font-weight:500}
.main-nav span::after{content:" ▾";font-size:11px}

/* hero slides */
.slide{position:absolute;left:0;width:1200px;height:544px;overflow:hidden}
.slide-1{top:126px;background:var(--hero-grey)}
.slide-2{top:670px;background:linear-gradient(135deg,#f4f4f4,#dcdcdc)}
.slide-3{top:1214px;background:var(--hero-grey)}
.slide-4{top:1758px;background:var(--hero-green)}
.tag{font-family:"Caveat Brush",cursive;font-size:38px;color:#fff}
.dark-text .tag{color:#333}
.title{font-family:"Archivo Black",sans-serif;color:#fff;font-size:54px;line-height:67px}
.dark-text .title{color:#3a3a3a}
.hl{background:var(--orange);color:#fff;padding:0 12px;display:inline-block}
.hl-dark{background:#333;color:var(--orange);padding:0 12px;display:inline-block}
.specs{font-size:15px;line-height:27.5px;font-weight:500;color:#fff}
.dark-text .specs{color:#333}
.btn-solid{display:inline-flex;align-items:center;gap:22px;background:var(--orange);color:#fff;font-size:16px;padding:0 22px;height:44px}
.btn-line{display:inline-flex;align-items:center;gap:22px;border:2px solid #333;color:#333;font-size:16px;padding:0 22px;height:44px}
.photo{position:absolute;border-radius:6px}
.feature{position:absolute;display:flex;align-items:center;gap:16px;color:#fff;font-weight:700;font-size:15px}
.feature i{width:40px;height:40px;border:2px solid var(--orange);border-radius:50%;display:block}
.dots{position:absolute;display:flex;gap:6px}
.dots b{display:block;height:3px;width:22px;background:#fff}
.dots b:first-child{width:50px;background:var(--orange)}

/* reviews */
.reviews{position:absolute;left:112px;top:2384px;width:976px;height:261px;border:1px solid #ccc}
.reviews-head{height:75px;border-bottom:1px solid #ccc;padding:18px 12px;font-family:"Caveat Brush",cursive;font-size:34px;color:#333}
.reviews-head em{font-style:normal;color:var(--orange)}
.arrows{position:absolute;right:14px;top:36px;display:flex;gap:10px}
.arrows i{display:block;width:22px;height:22px;border-radius:50%;background:var(--orange)}
.arrows i+i{width:18px;height:18px;background:#aaa;margin-top:2px}
.score{position:absolute;left:22px;top:108px;width:140px;text-align:center}
.score .badge{width:120px;height:52px;margin:0 auto 10px;background:var(--orange-4);border-radius:6px}
.score p{font-size:13px}
.review{position:absolute;top:112px;width:225px}
.review h4{font-size:18px;font-weight:500}
.stars{color:var(--orange);font-size:17px;letter-spacing:1px;margin:4px 0 8px}
.review p{font-size:12px;line-height:20px;color:#444}
.review p span{color:#999}

/* about */
.about{position:absolute;top:2726px;left:0;width:1200px;height:437px}
.about-text{position:absolute;left:318px;width:564px;height:437px;background:var(--about-bg);text-align:center;padding-top:60px}
.about-text .script{color:var(--orange);font-size:34px}
.about-text h2{font-family:"Archivo Black",sans-serif;font-size:54px;color:#333;line-height:66px}
.about-text p{font-size:15px;line-height:27.5px;color:#555;padding:12px 40px 16px}

/* newsletter */
.newsletter{position:absolute;top:3163px;left:0;width:1200px;height:451px;background:linear-gradient(110deg,#7b3b1d,#c06a34 45%,#d8a475 75%,#8d6a4f)}
.news-box{position:absolute;left:211px;top:104px;width:780px;height:259px;background:rgba(255,255,255,.93);text-align:center;padding-top:38px}
.news-box h3{font-family:"Caveat Brush",cursive;font-size:36px;color:#333;font-weight:400}
.news-box p{font-size:17px;margin-top:4px}
.news-form{display:flex;justify-content:center;gap:16px;margin-top:26px}
.news-form span{width:500px;height:50px;border:1px solid #ccc;background:#fff;text-align:left;padding:16px 20px;font-size:13px;color:#999}
.news-form b{width:138px;height:50px;background:var(--orange);color:#fff;font-size:15px;letter-spacing:1.5px;line-height:50px}

/* footer */
.site-footer{position:absolute;top:3614px;left:0;width:1200px;height:426px;background:var(--footer);color:#fff}
.col{position:absolute;top:44px}
.col h5{font-size:16px;font-weight:500;margin-bottom:14px}
.col li{list-style:none;font-size:12.5px;line-height:31px}
.contact-row{display:flex;gap:22px;font-size:14px;margin-bottom:20px;align-items:flex-start}
.contact-row svg{flex:none}
.footer-rule{position:absolute;left:112px;top:254px;width:976px;height:1px;background:#666}
.legal{position:absolute;left:112px;top:308px;font-size:13px;line-height:21px}
.vsep{position:absolute;top:290px;width:1px;height:66px;background:#666}
.footer-brand{position:absolute;left:424px;top:296px;font-family:"Archivo Black",sans-serif;color:var(--orange);font-size:38px;letter-spacing:3px;line-height:1}
.footer-brand small{display:block;font-size:14px;letter-spacing:10px;margin-top:6px;padding-left:90px}
.social{position:absolute;left:920px;top:313px;display:flex;gap:20px}
.social i{display:block;width:28px;height:28px;border-radius:50%;border:2px solid #fff}
.payments{position:absolute;top:4040px;left:0;width:1200px;height:79px;background:#fff;display:flex;justify-content:center;align-items:center;gap:26px;font-size:13px;font-weight:700;color:#333}
.payments span{display:flex;align-items:center;gap:6px}
.payments span::before{content:"";width:14px;height:14px;border-radius:50%;background:var(--orange-3)}
</style>
</head>
<body>

<header class="site-header">
  <div class="brand">IRONLINE<small>WORKWEAR</small></div>
  <div class="account">
    <svg width="26" height="26" viewBox="0 0 26 26"><circle cx="13" cy="13" r="13" fill="#222"/><circle cx="13" cy="10" r="5" fill="#fff"/><path d="M4 22c3-6 15-6 18 0" fill="#fff"/></svg>
    <span>Sign In or <a>Register</a></span>
  </div>
  <svg class="cart" width="26" height="26" viewBox="0 0 26 26"><path d="M4 8h16l-2 14H6z" fill="none" stroke="#222" stroke-width="2"/><path d="M8 8a4 4 0 0 1 8 0" fill="none" stroke="#222" stroke-width="2"/><circle cx="20" cy="7" r="5" fill="#ee7325"/></svg>
  <div class="search">Search
    <svg width="18" height="18" viewBox="0 0 18 18"><circle cx="7" cy="7" r="6" fill="#ee7325"/><path d="M11 11l6 6" stroke="#ee7325" stroke-width="3"/></svg>
  </div>
</header>

<nav class="main-nav">
  <span>WORK BOOTS</span><span>WORKWEAR</span><span>CUSTOMIZE IT</span><span>HARD HATS</span><span>GLOVES</span><span>HIGH VIS</span><span>SAFETY GLASSES</span><span>SEE MORE</span>
</nav>

<!-- slide 1 -->
<section class="slide slide-1">
  <div class="abs tag" style="left:110px;top:112px">Mens L/S</div>
  <h1 class="abs title" style="left:110px;top:170px">Standard<br>Vented Orange<br>Shirt</h1>
  <div class="abs btn-solid" style="left:110px;top:376px">Shop Now <span>⟶</span></div>
  <div class="photo" role="img" aria-label="Orange long-sleeve work shirt with reflective tape" style="left:565px;top:70px;width:290px;height:380px;background:linear-gradient(160deg,#ff8a2a,#e85f10)"></div>
  <div class="feature" style="left:850px;top:136px"><i></i>100% Cotton - Light Weight</div>
  <div class="feature" style="left:887px;top:238px"><i></i>Pre-Shrunk Drill Cotton</div>
  <div class="feature" style="left:870px;top:346px"><i></i>160 GSM (grams per sqM)</div>
  <div class="dots" style="left:542px;top:504px"><b></b><b></b><b></b></div>
</section>

<!-- slide 2 -->
<section class="slide slide-2 dark-text">
  <div class="photo" role="img" aria-label="Two-toned hi-vis orange and yellow shirts with navy lower panels" style="left:120px;top:90px;width:440px;height:350px;background:linear-gradient(90deg,#f07a1e 0 45%,#f2e02a 45% 100%)"></div>
  <div class="abs tag" style="left:620px;top:32px">Mens L/S</div>
  <h2 class="abs title" style="left:610px;top:88px"><span class="hl">TWO-TONED</span><br><span style="padding-left:10px">VENTED TAPED</span><br><span style="padding-left:10px">SHIRT</span></h2>
  <div class="abs specs" style="left:610px;top:288px">Two Chest Pockets<br>Back and Underarm Ventilation Mesh<br>Reflective Tape - Hoop Pattern<br>Suitable for Day Use (D/N Option available)<br>Compliant to AS/NZS 4602.1:2011<br>Compliant to AS/NZS 4399:2017 (UPF +50 Protection)</div>
  <div class="abs btn-line" style="left:610px;top:462px">Shop Now <span>⟶</span></div>
  <div class="dots" style="left:278px;top:504px"><b></b><b style="background:#fff"></b><b style="background:#fff"></b></div>
</section>

<!-- slide 3 -->
<section class="slide slide-3">
  <div class="abs tag" style="left:110px;top:30px">Mens L/S</div>
  <h2 class="abs title" style="left:100px;top:90px"><span class="hl-dark">Reflective</span><br><span style="padding-left:10px">Vented Orange</span><br><span style="padding-left:10px">Shirt</span></h2>
  <div class="abs specs" style="left:110px;top:288px">Two Chest Pockets<br>Back and Underarm Air Flow Ventilation Mesh<br>Biomotion Reflective Tape<br>Suitable for Day/Night Use<br>Compliant to AS/NZS 4602.1:2011<br>Compliant to AS/NZS 4399:2017 (UPF +50</div>
  <div class="abs btn-solid" style="left:112px;top:464px">Shop Now <span>⟶</span></div>
  <div class="photo" role="img" aria-label="Light orange reflective vented work shirt" style="left:555px;top:66px;width:300px;height:390px;background:linear-gradient(160deg,#ffb04f,#f08f2a)"></div>
  <div class="feature" style="left:850px;top:136px"><i></i>100% Cotton - Light Weight</div>
  <div class="feature" style="left:887px;top:238px"><i></i>Pre-Shrunk Drill Cotton</div>
  <div class="feature" style="left:870px;top:346px"><i></i>160 GSM (grams per sqM)</div>
</section>

<!-- slide 4 -->
<section class="slide slide-4 dark-text">
  <div class="photo" role="img" aria-label="Hi-vis yellow and orange long-sleeve polo shirts with navy panels" style="left:115px;top:68px;width:410px;height:400px;background:linear-gradient(90deg,#d8f34a 0 45%,#f78b2a 45% 100%)"></div>
  <div class="abs tag" style="left:620px;top:84px">Mens L/S</div>
  <h2 class="abs title" style="left:610px;top:140px"><span style="padding-left:10px">HI- VIS L/S</span><br><span class="hl">POLO</span></h2>
  <div class="abs specs" style="left:610px;top:288px">Contrast Striped Collar<br>Chest Pocket with Pen Insert<br>Suitable for Day Use<br>Compliant to AS/NZS 4602.1:2011</div>
  <div class="abs btn-line" style="left:610px;top:414px">Shop Now <span>⟶</span></div>
  <div class="dots" style="left:278px;top:504px"><b></b><b></b><b></b></div>
</section>

<!-- reviews -->
<section class="reviews">
  <div class="reviews-head"><em>What Our</em> Customers Are Saying</div>
  <div class="arrows"><i></i><i></i></div>
  <div class="score"><div class="badge"></div><p>Review Score 5.0 <span style="color:var(--orange)">★★★★★</span></p><p style="margin-top:6px">Based on <u>3,967 reviews</u></p></div>
  <div class="review" style="left:242px"><h4>Mara T. Quinlan</h4><div class="stars">★★★★★</div><p>Lorem Ipsum is simply dummy text of the printing and typesetting industry. Ever since the 1500s, <span>1 Day ago</span></p></div>
  <div class="review" style="left:491px"><h4>Mara T. Quinlan</h4><div class="stars">★★★★★</div><p>Lorem Ipsum is simply dummy text of the printing and typesetting industry. Ever since the 1500s, <span>1 Day ago</span></p></div>
  <div class="review" style="left:740px"><h4>Mara T. Quinlan</h4><div class="stars">★★★★★</div><p>Lorem Ipsum is simply dummy text of the printing and typesetting industry. Ever since the 1500s, <span>1 Day ago</span></p></div>
</section>

<!-- about -->
<section class="about">
  <div class="abs" role="img" aria-label="Construction workers in hard hats and orange workwear, seen from behind" style="left:0;top:0;width:318px;height:437px;background:linear-gradient(160deg,#5c6a72,#b44a2a 60%,#3d3a3a)"></div>
  <div class="about-text">
    <div class="script">About Us</div>
    <h2>Our Story</h2>
    <p>Lorem ipsum dolor sit amet, consectetur adipiscing elit, sed do eius-mod tempor incididunt ut labore et dolore magna aliqua. Ut enim ad minim veniam, quis nostrud exercitation ullamco laboris nisi ut aliquip ex ea commodo consequat. Duis aute irure dolor in reprehenderit in voluptate velit esse cillum dolore eu fugiat nulla pariatur.</p>
    <div class="btn-line">Read More <span>⟶</span></div>
  </div>
  <div class="abs" role="img" aria-label="Worker in orange coveralls and yellow hard hat overlooking a city" style="left:882px;top:0;width:318px;height:437px;background:linear-gradient(180deg,#d7d3cc,#8a8f94 60%,#4a4d52)"></div>
</section>

<!-- newsletter -->
<section class="newsletter" role="img" aria-label="Worker with tool belt on a construction site at sunset">
  <div class="news-box">
    <h3>Join our Newsletter</h3>
    <p>Eque porro quisquam est qui dolorem ipsum quia dolor sit amet</p>
    <div class="news-form"><span>Your Email Address</span><b>SUBSCRIBE</b></div>
  </div>
</section>

<!-- footer -->
<footer class="site-footer">
  <div class="col" style="left:112px">
    <h5>Contact Us</h5>
    <div class="contact-row"><svg width="16" height="20" viewBox="0 0 16 20"><path d="M8 0a7 7 0 0 1 7 7c0 5-7 13-7 13S1 12 1 7a7 7 0 0 1 7-7z" fill="#ee7325"/><circle cx="8" cy="7" r="2.5" fill="#353535"/></svg><div style="font-size:12.5px;line-height:21px">ADDRESS<br>812 Halden Avenue<br>Fairmont, OH 44100</div></div>
    <div class="contact-row"><svg width="18" height="18" viewBox="0 0 18 18"><path d="M4 1l4 4-2 2c1 2 3 4 5 5l2-2 4 4-2 3C8 17 1 10 1 4z" fill="#ee7325"/></svg>Phone: +1 555 014 227</div>
    <div class="contact-row"><svg width="18" height="14" viewBox="0 0 18 14"><rect width="18" height="14" fill="#ee7325"/><path d="M0 0l9 7 9-7" fill="none" stroke="#353535" stroke-width="1.5"/></svg>E-mail: info@ironlineworkwear.com</div>
  </div>
  <div class="col" style="left:555px"><h5>Quick links</h5><ul><li>Terms of Use</li><li>Privacy Policy</li><li>Payment Methods</li><li>Refund Policy</li></ul></div>
  <div class="col" style="left:761px"><h5>Quick links</h5><ul><li>Work Boots</li><li>Workwear</li><li>Customize It</li><li>Hard Hats</li><li>Gloves</li></ul></div>
  <div class="col" style="left:946px"><h5>My Account</h5><ul><li>Shipping</li><li>Contact Us</li><li>About us</li><li>Download our Catalogue</li></ul></div>
  <div class="footer-rule"></div>
  <div class="legal">Ironline Workwear © 2024.<br>All Rights Reserved.</div>
  <div class="vsep" style="left:368px"></div>
  <div class="footer-brand">IRONLINE<small>WORKWEAR</small></div>
  <div class="vsep" style="left:858px"></div>
  <div class="social" aria-label="Social links"><i></i><i></i><i></i><i></i></div>
</footer>

<div class="payments">
  <span>CardOne</span><span>TapPay</span><span>NorthCard</span><span>BluePass</span><span>CoinLine</span><span>SendFlow</span>
</div>

</body>
</html>
```